Convert web design from PDFs to Wordpress

I have designed the pages for my website in InDesign. I need someone to turn this into a Wordpress site. I will supply all graphics and photos and text, and the layout in PDF format.

To see PDFs of the designs we need converted to a Wordpress site, please send me an email at loricastel@mailbrook.net Thank you.

Please download PDF mockups, images, and fonts here: https://www.filecrate.net/s/kq7tmz831xpl4b2/RP%20site%20docs.zip?dl=0 After unzipping this file, you will find two folders: one for the home page, and one for the individual pages. Each folder has one PDF mockup, fonts, and linked images. Please install the included fonts so the PDF displays properly. Please see the PDF in each folder for the layout of each page. The PDFs include sticky notes with important instructions. If you previously received an email from me with PDF mockups, they are outdated: please replace those with the ones in this download link. Thank you.

This project has been completed. Not sure why Makerhive doesn't let designers know when a design has been accepted, so sorry if you didn't get the notice. Thank you for everyone who responded.

```html
<!DOCTYPE html>
<html lang="en">
<head>
<meta charset="utf-8">
<title>Harlan Reyes – Home</title>
<link rel="stylesheet" href="https://fonts.googleapis.com/css2?family=Open+Sans:ital,wght@0,400;0,600;0,700;1,700&display=swap">
<style>
  :root {
    --page-bg: #f4f5f7;
    --card-bg: #ffffff;
    --header-bg: #3f3f41;
    --divider: #cfcfcf;
    --brand-blue: #2aa7e0;
    --accent: #d3a472;
    --accent-soft: #e8cfae;
    --text-light: #ffffff;
    --text-muted: #5a5a5a;
    --text-dark: #3a3a3a;
    --star: #f2b632;
    --bar-empty: #e6e6e6;
    --note: #f4e43a;
    --note-edge: #3a3a1a;
  }
  * { box-sizing: border-box; margin: 0; padding: 0; }
  html, body { width: 1200px; height: 838px; overflow: hidden; }
  body { background: var(--page-bg); font-family: "Open Sans", Arial, sans-serif; position: relative; }

  .page { position: absolute; left: 15px; top: 28px; width: 1150px; height: 810px; background: var(--card-bg); }

  .site-header { position: absolute; left: 0; top: 0; width: 1150px; height: 115px; background: var(--header-bg); }
  .brand { position: absolute; left: 0; top: 0; width: 313px; height: 115px; border-right: 2px solid var(--divider);
    display: flex; align-items: center; justify-content: center; gap: 10px; }
  .brand-name { color: var(--brand-blue); font-size: 33px; font-weight: 400; letter-spacing: -0.5px; }
  .brand-mark { width: 12px; height: 12px; background: var(--brand-blue); }

  .main-nav { position: absolute; left: 357px; top: 0; height: 115px; display: flex; align-items: center; gap: 29px; }
  .main-nav a { color: var(--text-light); text-decoration: none; font-size: 13px; font-weight: 700; letter-spacing: 0.2px; }
  .main-nav a.current { color: var(--accent); }

  .call-box { position: absolute; left: 817px; top: 0; width: 333px; height: 115px; border-left: 2px solid var(--divider);
    text-align: center; color: var(--text-light); }
  .call-lead { margin-top: 18px; color: var(--accent); font-size: 12.5px; font-style: italic; font-weight: 700; }
  .call-number { font-size: 32px; font-weight: 600; line-height: 1.15; }
  .call-langs { font-size: 12.5px; font-weight: 600; margin-top: 2px; }

  .service-area { position: absolute; top: 128px; left: 0; width: 1150px; text-align: center;
    font-size: 16.5px; color: var(--text-muted); letter-spacing: -0.2px; }

  .hero-photo { position: absolute; left: 49px; top: 180px; width: 716px; height: 416px;
    background: linear-gradient(180deg, #f4f4f4 0%, #e4e4e6 45%, #3a3f4e 78%, #2c3140 100%); }
  .hero-tagline { position: absolute; left: 125px; top: 490px; width: 568px; height: 73px;
    border: 2px solid #e9e9e9; background: rgba(40,44,56,0.55); text-align: center; }
  .hero-tagline h2 { color: var(--accent); font-size: 34px; font-weight: 700; line-height: 1; margin-top: 8px; }
  .hero-tagline p { color: var(--text-light); font-size: 16px; margin-top: 3px; }

  .hero-rule { position: absolute; left: 0; top: 596px; width: 1150px; height: 8px; background: var(--header-bg); }

  .rating-card { position: absolute; left: 788px; top: 255px; width: 314px; height: 132px; background: #fff;
    box-shadow: 0 0 10px rgba(0,0,0,0.08); }
  .rating-score { position: absolute; left: 44px; top: 18px; font-size: 36px; color: var(--text-dark); }
  .rating-stars { position: absolute; left: 26px; top: 70px; }
  .rating-sources { position: absolute; left: 41px; top: 99px; display: flex; gap: 10px; }
  .rating-sources span { width: 14px; height: 14px; border-radius: 50%; background: #c9c9c9; }
  .rating-bars { position: absolute; left: 139px; top: 21px; }
  .bar-row { display: flex; align-items: center; height: 18.5px; font-size: 10px; color: #888; }
  .bar-row .lbl { width: 26px; }
  .bar-row .lbl b { color: var(--star); font-weight: 400; }
  .bar-row .track { width: 88px; height: 3px; background: var(--bar-empty); margin-right: 12px; }
  .bar-row .track.full { background: var(--star); }

  .reviews-btn { position: absolute; left: 857px; top: 431px; width: 176px; height: 25px; border-radius: 13px;
    background: var(--accent); color: var(--text-light); font-size: 12px; font-weight: 700; text-align: center; line-height: 25px; }

  .note { position: absolute; width: 22px; height: 18px; }

  .locations { position: absolute; left: 144px; top: 692px; }
  .locations h1 { font-size: 54px; font-weight: 400; color: var(--text-dark); letter-spacing: -0.5px; line-height: 1.1; }
  .locations p { font-size: 22px; color: var(--accent-soft); letter-spacing: -0.6px; margin-top: 6px; }
  .locations-rule { position: absolute; left: 144px; top: 801px; width: 861px; height: 3px; background: var(--accent-soft); }
</style>
</head>
<body>
<div class="page">
  <header class="site-header">
    <div class="brand"><span class="brand-mark"></span><span class="brand-name">Harlan Reyes</span></div>
    <nav class="main-nav">
      <a class="current" href="#">HOME</a><a href="#">WHAT WE DO</a><a href="#">ABOUT US</a><a href="#">FAQ</a><a href="#">CONTACT</a>
    </nav>
    <div class="call-box">
      <div class="call-lead">call today for your free consultation</div>
      <div class="call-number">(503) 555-0142</div>
      <div class="call-langs">se habla español &nbsp;|&nbsp; 讲中文</div>
    </div>
  </header>

  <div class="service-area">SERVING OREGON, WASHINGTON, AND THE ENTIRE PORTLAND METRO AREA</div>

  <div class="hero-photo" role="img" aria-label="Team photo of the four firm attorneys in dark suits against a white background"></div>
  <div class="hero-tagline">
    <h2>Experience. Efficiency. Results.</h2>
    <p>...and yes, you can reach us by phone.</p>
  </div>
  <div class="hero-rule"></div>

  <div class="rating-card">
    <div class="rating-score">5.0</div>
    <svg class="rating-stars" width="96" height="18" viewBox="0 0 96 18" aria-hidden="true">
      <defs><polygon id="star" points="9,0 11.6,6 18,6.5 13.2,10.8 14.6,17 9,13.7 3.4,17 4.8,10.8 0,6.5 6.4,6" fill="#f2b632"/></defs>
      <use href="#star" x="0"/><use href="#star" x="19.5"/><use href="#star" x="39"/><use href="#star" x="58.5"/><use href="#star" x="78"/>
    </svg>
    <div class="rating-sources"><span></span><span></span><span></span></div>
    <div class="rating-bars">
      <div class="bar-row"><span class="lbl">5 <b>★</b></span><span class="track full"></span>14</div>
      <div class="bar-row"><span class="lbl">4 <b>★</b></span><span class="track"></span>0</div>
      <div class="bar-row"><span class="lbl">3 <b>★</b></span><span class="track"></span>0</div>
      <div class="bar-row"><span class="lbl">2 <b>★</b></span><span class="track"></span>0</div>
      <div class="bar-row"><span class="lbl">1 <b>★</b></span><span class="track"></span>0</div>
    </div>
  </div>

  <div class="reviews-btn">READ OUR REVIEWS</div>

  <svg class="note" style="left:844px;top:182px" viewBox="0 0 22 18" aria-hidden="true">
    <path d="M2 1h18a1 1 0 0 1 1 1v10a1 1 0 0 1-1 1H8l-4 4v-4H2a1 1 0 0 1-1-1V2a1 1 0 0 1 1-1z" fill="#f4e43a" stroke="#3a3a1a" stroke-width="1.3"/>
    <path d="M5 5h12M5 8h12" stroke="#3a3a1a" stroke-width="1"/>
  </svg>
  <svg class="note" style="left:1022px;top:318px" viewBox="0 0 22 18" aria-hidden="true">
    <path d="M2 1h18a1 1 0 0 1 1 1v10a1 1 0 0 1-1 1H8l-4 4v-4H2a1 1 0 0 1-1-1V2a1 1 0 0 1 1-1z" fill="#f4e43a" stroke="#3a3a1a" stroke-width="1.3"/>
    <path d="M5 5h12M5 8h12" stroke="#3a3a1a" stroke-width="1"/>
  </svg>
  <svg class="note" style="left:1042px;top:439px" viewBox="0 0 22 18" aria-hidden="true">
    <path d="M2 1h18a1 1 0 0 1 1 1v10a1 1 0 0 1-1 1H8l-4 4v-4H2a1 1 0 0 1-1-1V2a1 1 0 0 1 1-1z" fill="#f4e43a" stroke="#3a3a1a" stroke-width="1.3"/>
    <path d="M5 5h12M5 8h12" stroke="#3a3a1a" stroke-width="1"/>
  </svg>

  <section class="locations">
    <h1>One firm, two locations</h1>
    <p>GRESHAM AND HILLSBORO PERSONAL INJURY LAWYERS</p>
  </section>
  <div class="locations-rule"></div>
</div>
</body>
</html>
```